Sticker for Luxury Men Underwear

Hello there,

We would like to design a strong, sexy, masculine, modern sticker for our new luxury underwear packaging.

The package pictures are attached. It is a silver sleeve. The sticker/artwork dimension should be 7 inches tall per 5 inches large. Also, Attached are the sketches of the underwear for your reference.

Open to package with or without model shot. Ideas attached.

Thank you,

Torven
www.brelvantwear.com (under construction)

Thank you Everyone for your designs that were submitted. At this time we are putting the work on hold until we can have our photo shoot completed to allow our designers to work with our pictures. 

We will be in contact with you as soon as we have the pictures available. 

Reason: Waiting for the pictures from the photoshoot. Project will resume once received. Thanks

Reason: Waiting for photoshoot pictures - will be 3/4 more weeks.

Reason: Still waiting for photoshoot pictures. Photoshoot is scheduled for september 8th.

Reason: still waiting for the pictures - coming soon.

Target Market(s)

High fashion, young, stylish, trendy, masculine guys

Industry/Entity Type

Construction

Requirements
Must have
• - Product Identity Declaration (Boxer brief/Brief/Trunks)
- Logo
- Size (S/M/L)
- Color
- Barcode
- Name and Place of Business: Brelvant Wear Ltd, Vancouver, BC, V5K 3 P8 - CA 83426
- website: www.brelvantwear.com

- size table?
- care label?
- fabric composition?
Nice to have
• Sexy/Elegant
masculine
Strong
modern
sleek

```html
<!DOCTYPE html>
<html lang="en">
<head>
<meta charset="utf-8">
<title>Brelvant Wear – Boxer Brief Sticker</title>
<link rel="stylesheet" href="https://fonts.googleapis.com/css2?family=Archivo+Narrow:wght@400;700&display=swap">
<style>
  :root {
    --page-bg: #f2f2f2;
    --sticker-black: #0b0b0b;
    --logo-white: #ffffff;
    --spec-white: #ffffff;
    --photo-light: #e9e6e3;
    --photo-mid: #d9c2ad;
    --photo-skin: #c99a78;
    --garment-white: #f4f4f4;
  }
  * { box-sizing: border-box; margin: 0; padding: 0; }
  html, body {
    width: 1200px;
    height: 900px;
    overflow: hidden;
    background: var(--page-bg);
    font-family: "Archivo Narrow", "Arial Narrow", sans-serif;
  }
  .sticker {
    position: absolute;
    left: 320px;
    top: 60px;
    width: 560px;
    height: 780px;
    border-radius: 8px 34px 26px 26px;
    overflow: hidden;
    background: var(--sticker-black);
    border-left: 6px solid var(--sticker-black);
  }
  .model-photo {
    position: absolute;
    left: 0;
    top: 0;
    width: 100%;
    height: 604px;
    background:
      radial-gradient(ellipse 60% 45% at 55% 40%, var(--photo-skin) 0%, var(--photo-mid) 55%, transparent 80%),
      linear-gradient(180deg, var(--photo-light) 0%, var(--photo-mid) 100%);
  }
  .brand-name {
    position: absolute;
    left: 22px;
    bottom: 182px;
    width: 516px;
    font-weight: 700;
    font-size: 128px;
    line-height: 1;
    letter-spacing: -1px;
    color: var(--logo-white);
    text-align: center;
  }
  .info-band {
    position: absolute;
    left: 0;
    bottom: 0;
    width: 100%;
    height: 176px;
    background: var(--sticker-black);
  }
  .product-spec {
    position: absolute;
    left: 236px;
    top: 56px;
    color: var(--spec-white);
    font-weight: 700;
    font-size: 15px;
    line-height: 1.15;
    list-style: none;
  }
  .garment-sketch {
    position: absolute;
    left: 368px;
    top: 18px;
    width: 150px;
    height: 116px;
    border-radius: 6px;
    background: linear-gradient(180deg, var(--garment-white) 0%, #dcdcdc 100%);
  }
</style>
</head>
<body>
  <main class="sticker">
    <div class="model-photo" role="img" aria-label="Photo of a model's torso wearing white boxer briefs with a logo waistband"></div>
    <div class="brand-name">BRELVANT</div>
    <section class="info-band">
      <ul class="product-spec">
        <li>Size M</li>
        <li>Boxer brief</li>
        <li>White</li>
      </ul>
      <div class="garment-sketch" role="img" aria-label="Technical sketch of the white boxer brief, front view"></div>
    </section>
  </main>
</body>
</html>
```